Cards
technology and consulting.
Project: Cards
Cards -
Creative Brief
Modern
Dennis Harlow
4173 Alder Lane Muskegon, MI 49467
harlowd@bizandgrowth.example
www.bizandgrowth.example

```html
<!DOCTYPE html>
<html lang="en">
<head>
<meta charset="utf-8">
<title>Biz &amp; Growth – Business Card</title>
<link rel="stylesheet" href="https://fonts.googleapis.com/css2?family=Michroma&family=Questrial&display=swap">
<style>
  :root {
    --backdrop: #262626;
    --card-white: #ffffff;
    --navy-deep: #071a52;
    --navy-mid: #0d2a72;
    --navy-ink: #0b2566;
    --accent-blue: #3fa2ff;
    --text-light: #ffffff;
  }
  * { margin: 0; padding: 0; box-sizing: border-box; }
  html, body {
    width: 1200px;
    height: 797px;
    overflow: hidden;
    background: var(--backdrop);
  }
  .canvas {
    position: relative;
    width: 1200px;
    height: 797px;
  }
  .card {
    position: absolute;
    left: 60px;
    top: 50px;
    width: 1080px;
    height: 620px;
    overflow: hidden;
    background: radial-gradient(ellipse at 30% 60%, var(--navy-mid) 0%, var(--navy-deep) 75%);
  }
  .card__header {
    position: absolute;
    left: 0;
    top: 0;
    width: 100%;
    height: 199px;
    background: var(--card-white);
  }
  .brand {
    position: absolute;
    left: 40px;
    top: 66px;
    display: flex;
    align-items: center;
    gap: 22px;
  }
  .brand__square {
    width: 62px;
    height: 62px;
    background: var(--navy-ink);
  }
  .brand__name {
    font-family: "Questrial", sans-serif;
    font-size: 58px;
    color: var(--navy-ink);
    letter-spacing: 2px;
    line-height: 1;
  }
  .contact {
    position: absolute;
    left: 427px;
    top: 396px;
    color: var(--text-light);
  }
  .contact__name {
    font-family: "Michroma", sans-serif;
    font-size: 33px;
    letter-spacing: 1px;
    line-height: 48px;
    text-transform: uppercase;
  }
  .contact__list {
    list-style: none;
    margin-top: 14px;
    font-family: "Questrial", sans-serif;
    font-size: 29px;
  }
  .contact__row {
    display: flex;
    height: 35px;
    line-height: 35px;
  }
  .contact__label { width: 106px; }
  .accent-rules {
    position: absolute;
    left: 0;
    top: 0;
  }
</style>
</head>
<body>
<div class="canvas">
  <div class="card">
    <div class="card__header">
      <div class="brand">
        <span class="brand__square"></span>
        <span class="brand__name">BIZ &amp; GROWTH</span>
      </div>
    </div>

    <svg class="accent-rules" width="1080" height="620" viewBox="0 0 1080 620" aria-hidden="true">
      <defs>
        <linearGradient id="rule-fade" x1="0" y1="0" x2="0" y2="1">
          <stop offset="0" stop-color="#3fa2ff" stop-opacity="0.2"/>
          <stop offset="0.5" stop-color="#3fa2ff" stop-opacity="1"/>
          <stop offset="1" stop-color="#3fa2ff" stop-opacity="0.2"/>
        </linearGradient>
      </defs>
      <rect x="390" y="398" width="3" height="62" fill="url(#rule-fade)"/>
      <rect x="390" y="468" width="3" height="132" fill="url(#rule-fade)"/>
    </svg>

    <div class="contact">
      <h1 class="contact__name">Dennis Harlow</h1>
      <ul class="contact__list">
        <li class="contact__row"><span class="contact__label">Phone</span><span>231.555.0187</span></li>
        <li class="contact__row"><span class="contact__label">Email</span><span>harlowd@bizandgrowth.example</span></li>
        <li class="contact__row"><span class="contact__label">Web</span><span>www.bizandgrowth.example</span></li>
        <li class="contact__row"><span class="contact__label">Add</span><span>4173 Alder Lane Muskegon, MI 49467</span></li>
      </ul>
    </div>
  </div>
</div>
</body>
</html>
```